Business Cards

We were billed for this because the project timed out. Please give me another designed to open this back up. I was not happy with the last designs (that I was charged for).
we are also using the logo with Revitalizing Pools One Drop at a Time
Also want to utilize Where Healthy Water is our Commitment.

Contact Information for Business Card

Marlowe Stone Group Inc

```html
<!DOCTYPE html>
<html lang="en">
<head>
<meta charset="utf-8">
<title>Marlowe Stone Group – Business Cards</title>
<link rel="stylesheet" href="https://fonts.googleapis.com/css2?family=Montserrat:wght@400;500;700;800&display=swap">
<style>
  :root {
    --page-bg: #d6d6d6;
    --blue-light: #6aa3d0;
    --blue-mid: #3f87c0;
    --blue-deep: #0f69b1;
    --card-white: #f1f1f1;
    --card-white-edge: #e6e6e6;
    --text-dark: #2f2f2f;
    --text-grey: #5a5a5a;
    --accent-blue: #2f7bbf;
  }
  * { box-sizing: border-box; margin: 0; padding: 0; }
  html, body {
    width: 1200px; height: 1200px; overflow: hidden;
    background: var(--page-bg);
    font-family: "Montserrat", sans-serif;
  }
  .sheet {
    width: 1200px; height: 1200px;
    display: flex; flex-direction: column; align-items: center; justify-content: center;
    gap: 64px;
  }
  .card {
    width: 770px; height: 440px;
    border-radius: 26px;
    position: relative;
    box-shadow: 0 10px 24px rgba(0,0,0,0.18);
  }
  .card--front {
    background: linear-gradient(90deg, var(--blue-light) 0%, var(--blue-mid) 38%, var(--blue-deep) 72%, var(--blue-deep) 100%);
    display: flex; align-items: center; justify-content: center;
  }
  .brand-name {
    color: #ffffff;
    font-weight: 800;
    font-size: 44px;
    letter-spacing: 5px;
    text-transform: uppercase;
    white-space: nowrap;
  }
  .card--back {
    background: linear-gradient(135deg, var(--card-white) 0%, var(--card-white-edge) 100%);
  }
  .back-brand {
    position: absolute; top: 60px; right: 56px;
    color: var(--text-dark);
    font-weight: 800;
    font-size: 24px;
    letter-spacing: 3px;
    text-transform: uppercase;
    white-space: nowrap;
  }
  .contact-block {
    position: absolute; left: 56px; bottom: 44px;
  }
  .person-name {
    color: var(--accent-blue);
    font-weight: 700;
    font-size: 38px;
    line-height: 1.1;
  }
  .person-title {
    color: var(--text-grey);
    font-size: 20px;
    font-weight: 500;
    margin: 6px 0 12px;
  }
  .contact-list { list-style: none; }
  .contact-list li {
    display: flex; align-items: center; gap: 12px;
    color: var(--text-dark);
    font-size: 20px;
    line-height: 34px;
    white-space: nowrap;
  }
  .contact-icon { width: 18px; height: 18px; flex: none; }
  .address {
    position: absolute; right: 56px; top: 262px;
    text-align: right;
    color: var(--text-dark);
    font-size: 20px;
    line-height: 32px;
    font-style: normal;
    white-space: nowrap;
  }
</style>
</head>
<body>
<main class="sheet">
  <section class="card card--front" aria-label="Card front">
    <span class="brand-name">Marlowe Stone Group</span>
  </section>

  <section class="card card--back" aria-label="Card back">
    <span class="back-brand">Marlowe Stone Group</span>

    <div class="contact-block">
      <h1 class="person-name">Everett Lane</h1>
      <p class="person-title">Founder &amp; Director</p>
      <ul class="contact-list">
        <li>
          <svg class="contact-icon" viewBox="0 0 24 24" aria-hidden="true">
            <path fill="#2f7bbf" d="M6.6 10.8a15.1 15.1 0 0 0 6.6 6.6l2.2-2.2a1 1 0 0 1 1-.25 11.4 11.4 0 0 0 3.6.57 1 1 0 0 1 1 1V20a1 1 0 0 1-1 1A17 17 0 0 1 3 4a1 1 0 0 1 1-1h3.5a1 1 0 0 1 1 1c0 1.25.2 2.450.57 3.6a1 1 0 0 1-.25 1z"/>
          </svg>
          (405)-555-0142
        </li>
        <li>
          <svg class="contact-icon" viewBox="0 0 24 24" aria-hidden="true">
            <rect x="2" y="5" width="20" height="14" rx="1.5" fill="#2f7bbf"/>
            <path d="M3 6.5l9 6.5 9-6.5" fill="none" stroke="#f1f1f1" stroke-width="1.6"/>
          </svg>
          lane@marlowestonegroup.com
        </li>
        <li>
          <svg class="contact-icon" viewBox="0 0 24 24" aria-hidden="true">
            <circle cx="12" cy="12" r="10" fill="#2f7bbf"/>
            <g fill="none" stroke="#f1f1f1" stroke-width="1.4">
              <ellipse cx="12" cy="12" rx="4.2" ry="10"/>
              <path d="M2 12h20M4 7h16M4 17h16"/>
            </g>
          </svg>
          www.marlowestonegroup.com
        </li>
      </ul>
    </div>

    <address class="address">
      4170 Harbor Lane<br>
      Cedar Falls Maine 04021
    </address>
  </section>
</main>
</body>
</html>
```